Design some Business Cards

I NEED A BUSINESS CARD DESIGN AND A [login to view URL] IS MY OLD LOGO BUT USE YOUR CREATIVITY TO CREATE A DIFFERENT ONE (PICTURES ATTACHED).DESIGN A NEW LOGO AND BUSINESS CARD.
CHANGE EMAIL to derek@[login to view URL]
add address: Guelph,Ontario
phone and and fax remain the same.

```html
<!DOCTYPE html>
<html lang="en">
<head>
<meta charset="utf-8">
<title>Derek Hartwell – Business Cards</title>
<link rel="stylesheet" href="https://fonts.googleapis.com/css2?family=Source+Sans+3:wght@400;700&display=swap">
<style>
  :root {
    --page: #f8f2ea;
    --card: #050505;
    --accent: #8fe04a;
    --ink-light: #e8e8e8;
    --shadow: rgba(0, 0, 0, 0.35);
  }
  * { margin: 0; padding: 0; box-sizing: border-box; }
  html, body { width: 1200px; height: 1200px; overflow: hidden; }
  body {
    background: var(--page);
    font-family: "Source Sans 3", "Helvetica Neue", Arial, sans-serif;
    position: relative;
  }
  .card {
    position: absolute;
    top: 151px;
    width: 468px;
    height: 245px;
    background: var(--card);
    box-shadow: 2px 3px 6px var(--shadow);
    overflow: hidden;
  }
  .card--front { left: 144px; }
  .card--back { left: 624px; }
  .card__lines {
    position: absolute; inset: 0;
    width: 100%; height: 100%;
  }
  .card__lines line {
    stroke: var(--accent);
    stroke-width: 3;
  }
  .brand-dot {
    position: absolute;
    border-radius: 50%;
    background: var(--accent);
  }
  .brand-name {
    position: absolute;
    color: var(--accent);
    font-weight: 700;
    text-transform: uppercase;
    white-space: nowrap;
    line-height: 1;
  }
  .brand-tagline {
    position: absolute;
    color: var(--accent);
    font-weight: 700;
    text-transform: uppercase;
    white-space: nowrap;
    line-height: 1;
  }
  /* front */
  .card--front .brand-dot { left: 202px; top: 19px; width: 100px; height: 100px; }
  .card--front .brand-name { left: 0; width: 100%; text-align: center; top: 124px; font-size: 30px; letter-spacing: 0.5px; }
  .card--front .brand-tagline { left: 0; width: 100%; text-align: center; top: 156px; font-size: 10px; letter-spacing: 0.3px; }
  /* back */
  .card--back .brand-dot { left: 84px; top: 5px; width: 46px; height: 46px; }
  .card--back .brand-name { left: 136px; top: 14px; font-size: 22px; }
  .card--back .brand-tagline { left: 137px; top: 38px; font-size: 7.5px; }
  .contact-list {
    position: absolute;
    left: 22px;
    top: 140px;
    list-style: none;
  }
  .contact-list li {
    display: flex;
    align-items: center;
    gap: 6px;
    height: 18px;
    color: var(--ink-light);
    font-size: 11px;
  }
  .contact-list li.contact--email { font-size: 9px; margin-bottom: 4px; }
  .contact-icon { width: 14px; height: 14px; flex: none; }
  .contact-icon * { fill: none; stroke: var(--ink-light); stroke-width: 1.4; }
</style>
</head>
<body>

  <section class="card card--front" aria-label="Card front">
    <svg class="card__lines" viewBox="0 0 468 245" aria-hidden="true">
      <line x1="3" y1="73" x2="85" y2="3"/>
      <line x1="7" y1="109" x2="109" y2="3"/>
      <line x1="361" y1="3" x2="441" y2="76"/>
      <line x1="395" y1="3" x2="461" y2="63"/>
      <line x1="0" y1="207" x2="468" y2="207"/>
      <line x1="0" y1="220" x2="468" y2="220"/>
    </svg>
    <span class="brand-dot"></span>
    <h1 class="brand-name">Derek Hartwell</h1>
    <p class="brand-tagline">Custom Homes &amp; Renovations</p>
  </section>

  <section class="card card--back" aria-label="Card back">
    <svg class="card__lines" viewBox="0 0 468 245" aria-hidden="true">
      <line x1="3" y1="76" x2="76" y2="3"/>
      <line x1="303" y1="3" x2="467" y2="167"/>
      <line x1="309" y1="49" x2="462" y2="202"/>
      <line x1="203" y1="200" x2="329" y2="76"/>
      <line x1="0" y1="207" x2="468" y2="207"/>
      <line x1="0" y1="215" x2="468" y2="215"/>
    </svg>
    <span class="brand-dot"></span>
    <h2 class="brand-name">Derek Hartwell</h2>
    <p class="brand-tagline">Custom Homes &amp; Renovations</p>
    <ul class="contact-list">
      <li class="contact--email">
        <svg class="contact-icon" viewBox="0 0 14 14" aria-hidden="true"><rect x="1" y="3" width="12" height="8"/><polyline points="1,3 7,8 13,3"/></svg>
        derek@hartwellhomes.com
      </li>
      <li class="contact--phone">
        <svg class="contact-icon" viewBox="0 0 14 14" aria-hidden="true"><path d="M3 1 L5 1 L6 4 L4.5 5.5 Q6 8.5 8.5 9.5 L10 8 L13 9 L13 11 Q12 13 10 13 Q2 11 1 3 Q1 1 3 1 Z"/></svg>
        555.310.0142
      </li>
      <li class="contact--fax">
        <svg class="contact-icon" viewBox="0 0 14 14" aria-hidden="true"><rect x="3" y="1" width="8" height="4"/><rect x="1" y="5" width="12" height="6"/><rect x="3" y="9" width="8" height="4"/></svg>
        555.310.0187
      </li>
    </ul>
  </section>

</body>
</html>
```